Manufacturer of prepared Persian ready meals needs a product concept design

I need a product concept design for a new company based in the UK called 'Velmora Foods Ltd'.
The winner will potentially be selected to produce prototype designs for our other products.
For this project, the product will be called "Ghormeh Sabzi". This needs to be on the design to let consumers know what it is.
Whilst still in the concept stage, the aim of the company is to produce refrigerated microwaveable / oven Persian ready meal for retail supermarket consumers, and may also have an online platform for direct to consumer sales.
I have provided quite a few competitor examples of products.
I would like the product in a black or clear round bowl. It will be split into two sections (Half stew / Half rice) by the sleeve, which you are designing. I would like the food to be visible on either side of the label, so the consumer knows what they are eating.
The logo is provided within the file attachments and needs to be on prominent display on the pouch.
The mission for Velmora Foods Ltd brand is:
"Bringing 2,500 years of scented history to your table".
This needs to be present on the sleeve.
The product needs to represent the ethnicity of the brand throughout the design, and the same font to be used throughout.
Persian architecture was filled with a wide range of vibrant colours and has been engineered to stand the test of time, so I would like that to be incorporated into the product design (see attached examples of Persian geometry).
Alternatively Persian carpets are world renowned for their quality, so examples of this could be displayed on the packaging.
These will have to be artistically interpreted to avoid potential copyright; I am looking for individual artistic design.
It needs to represent a super quality, royalty & decadence throughout, and stand out on the shelves to the consumer above all the other competitor products.
To comply with food standards, the sleeve must have a nutritional label on display. I have attached a generic example for you to use. You may create your own representation of it.
Ghormeh Sabzi is a natural source of fibre, high in protein, gluten and dairy free, so I would like this displayed on the sleeve, as well as the the words:
- Traditionally rich in aromatic herbs, tender slow cooked lamb, red kidney beans & dried limes
- One of the oldest dishes in Persian history
You can find pictures of the food provided in the files. Note, these are not my pictures, but give you an idea of what will be provided inside.
Some designers have uploaded the same design up to 5 times, others twice. Only 18 have been uploaded, but it says 20, so I think 2 have been removed?

```html
<!DOCTYPE html>
<html lang="en">
<head>
<meta charset="utf-8">
<title>Velmora Foods – Ghormeh Sabzi sleeve</title>
<link rel="stylesheet" href="https://fonts.googleapis.com/css2?family=Bebas+Neue&family=Montserrat:ital,wght@0,300;0,400;0,600;0,700;1,600&display=swap">
<style>
  :root {
    --sleeve-green: #00a04b;
    --pattern-green: #049446;
    --title-green: #00984a;
    --brand-yellow: #fff200;
    --label-yellow: #f4ea1a;
    --ink-dark: #2b1a4a;
    --white: #ffffff;
    --page: #f4f4f4;
    --cal: #f0573a;
    --sodium: #1fc4c4;
    --sugar: #f9b20f;
    --fat: #6b3190;
    --salt: #f79a7c;
  }
  * { box-sizing: border-box; margin: 0; padding: 0; }
  html, body { width: 1200px; height: 1200px; overflow: hidden; background: var(--page); }
  body { font-family: "Montserrat", sans-serif; position: relative; }

  .sleeve {
    position: absolute; left: 175px; top: 67px;
    width: 849px; height: 1066px;
    background: var(--sleeve-green);
    overflow: hidden; color: var(--white);
  }
  .sleeve__pattern {
    position: absolute; inset: 0;
    background: radial-gradient(circle at 50% 40%, var(--sleeve-green) 0%, var(--pattern-green) 100%);
  }
  .brand-mark {
    position: absolute; left: 352px; top: 70px;
    width: 150px; height: 150px;
    border: 6px solid var(--brand-yellow);
  }
  .brand-name {
    position: absolute; left: 0; width: 100%; text-align: center;
    font-family: "Montserrat", sans-serif; font-weight: 700; color: var(--white);
  }
  .brand-name--main { top: 285px; font-size: 86px; letter-spacing: 26px; text-indent: 26px; line-height: 1; }
  .brand-name--sub { top: 378px; font-size: 40px; letter-spacing: 30px; text-indent: 30px; line-height: 1; }
  .mission {
    position: absolute; top: 437px; width: 100%; text-align: center;
    font-style: italic; font-weight: 600; font-size: 18.5px;
  }
  .title-band {
    position: absolute; top: 509px; left: 0; width: 100%; height: 181px;
    background: var(--brand-yellow);
  }
  .title-band svg { display: block; }
  .description {
    position: absolute; top: 705px; width: 100%; text-align: center;
    font-weight: 400; font-size: 21px; line-height: 28px;
  }
  .heritage {
    position: absolute; top: 791px; width: 100%; text-align: center;
    font-style: italic; font-weight: 600; font-size: 21px; color: var(--brand-yellow);
  }
  .nutrition { position: absolute; left: 95px; top: 852px; width: 380px; text-align: center; }
  .nutrition__title { font-weight: 600; font-size: 17px; letter-spacing: .5px; line-height: 22px; }
  .nutrition__serving { font-weight: 300; font-size: 14px; line-height: 18px; }
  .nutrition__row { display: block; margin: 8px auto 0; }
  .nutrition__note { font-weight: 300; font-size: 14px; line-height: 18px; margin-top: 4px; }
  .claims {
    position: absolute; left: 506px; top: 905px; width: 343px; height: 93px;
    background: var(--label-yellow); border-radius: 46px 0 0 46px;
  }
  .claims svg { display: block; }
</style>
</head>
<body>
  <main class="sleeve">
    <div class="sleeve__pattern" role="img" aria-label="Persian floral geometric pattern in tonal greens"></div>

    <div class="brand-mark" aria-hidden="true"></div>
    <div class="brand-name brand-name--main">VELMORA</div>
    <div class="brand-name brand-name--sub">FOODS</div>
    <p class="mission">Bringing 2,500 years of scented history to your table</p>

    <div class="title-band">
      <svg width="849" height="181" viewBox="0 0 849 181">
        <text x="50" y="158" textLength="748" lengthAdjust="spacingAndGlyphs"
              font-family="Bebas Neue, sans-serif" font-size="190" fill="#00984a">GHORMEH SABZI</text>
      </svg>
    </div>

    <p class="description">Traditionally rich in aromatic herbs, tender slow cooked lamb,<br>red kidney beans &amp; dried limes</p>
    <p class="heritage">One of the oldest dishes in Persian history</p>

    <section class="nutrition">
      <h2 class="nutrition__title">NUTRITIONAL FACTS</h2>
      <p class="nutrition__serving">Each serving (150g) contains</p>
      <svg class="nutrition__row" width="360" height="92" viewBox="0 0 360 92" font-family="Montserrat, sans-serif">
        <defs>
          <g id="gda-shell">
            <path d="M2,30 A26.5,26.5 0 0 1 55,30 V72 H2 Z" fill="#fff" stroke="#2b1a4a" stroke-width="3.5"/>
            <rect x="10" y="70" width="37" height="19" rx="9.5" fill="#fff" stroke="#2b1a4a" stroke-width="3"/>
            <text x="26" y="35" font-size="19" font-weight="700" fill="#2b1a4a" text-anchor="middle">250<tspan font-size="6">kJ</tspan></text>
            <text x="28.5" y="84" font-size="11" font-weight="600" fill="#2b1a4a" text-anchor="middle">0,5%</text>
          </g>
        </defs>
        <g transform="translate(3,0)"><use href="#gda-shell"/><rect x="4" y="43" width="49" height="17" fill="var(--cal)"/><text x="28.5" y="55.5" font-size="10" font-weight="600" fill="#fff" text-anchor="middle">Calories</text></g>
        <g transform="translate(75,0)"><use href="#gda-shell"/><rect x="4" y="43" width="49" height="17" fill="var(--sodium)"/><text x="28.5" y="55.5" font-size="10" font-weight="600" fill="#fff" text-anchor="middle">Sodium</text></g>
        <g transform="translate(147,0)"><use href="#gda-shell"/><rect x="4" y="43" width="49" height="17" fill="var(--sugar)"/><text x="28.5" y="55.5" font-size="10" font-weight="600" fill="#fff" text-anchor="middle">Sugar</text></g>
        <g transform="translate(219,0)"><use href="#gda-shell"/><rect x="4" y="43" width="49" height="17" fill="var(--fat)"/><text x="28.5" y="55.5" font-size="10" font-weight="600" fill="#fff" text-anchor="middle">Fat</text></g>
        <g transform="translate(291,0)"><use href="#gda-shell"/><rect x="4" y="43" width="49" height="17" fill="var(--salt)"/><text x="28.5" y="55.5" font-size="10" font-weight="600" fill="#fff" text-anchor="middle">Salt</text></g>
      </svg>
      <p class="nutrition__note">of an adult's reference intake<br>Typical values (as sold) per 100g: 697kJ/167kCal</p>
    </section>

    <div class="claims">
      <svg width="343" height="93" viewBox="0 0 343 93" font-family="Montserrat, sans-serif" font-weight="700" fill="#00984a">
        <g fill="#fff" stroke="#00a04b" stroke-width="4">
          <circle cx="52" cy="48" r="27"/><circle cx="122" cy="48" r="27"/>
          <circle cx="193" cy="48" r="27"/><circle cx="263" cy="48" r="27"/>
        </g>
        <g font-size="7" text-anchor="middle">
          <text x="52" y="41">NATURAL</text><text x="52" y="50">SOURCE</text><text x="52" y="59">OF FIBRE</text>
          <text x="122" y="46">HIGH IN</text><text x="122" y="55">PROTEIN</text>
          <text x="193" y="46">GLUTEN</text><text x="193" y="55">FREE</text>
          <text x="263" y="46">DAIRY</text><text x="263" y="55">FREE</text>
        </g>
      </svg>
    </div>
  </main>
</body>
</html>
```